Gutschein-Design zur Pflegeberatung
Zielgruppe
Wir feiern mit unserem Pflegedienst das 10 Jährige Jubiläum. Da es wegen der Corona Pandemie keine Feierlichkeiten geben kann, würde ich wir einen Gutschein für eine kostenlose Pflegeberatung erstellen lassen. Auf die Vorderseite bitte den Gutschein mit dem Text:
Bilder bitte aus den öffentlichen Portalen verwenden.
Gutschein zur Pflegeberatung
Wir unterstützen bei der Beantragung eines Pflegegrades und helfen bei abgelehnten Anträgen.
Gerne informieren wir Sie über umfangreiche Möglichkeiten der ambulante Pflege und erstellen einen individuellen Versorgungsplan. Darüber hinaus erhalte Sie praktische Tipps zu Alltagshilfen und konkrete Hilfestellungen rund um die Pflege, damit Sie noch so lange wie möglich zu
Hause bleiben können.
Unten bitte einfügen: Gutschein gültig bis einschließlich Juli 2022
Auf die Rückseite bitte eine kurze Info zu unserem 10 Jährigen bestehen.
Vielleicht vielleicht wieder mit dem Slogan, Seit 10 Jahren rund um die Uhr für Sie im Einsatz.
Aufgabenstellung
Da wir zwei ambulante Filialen betreiben, muss das Logo auf die zweite Filiale angepasst werden.
Der Text und die Informationen bleiben jedoch gleich. Der Gutschein sollte sofort auffallen und animieren, im Pflegedienst anzurufen.

```html
<!DOCTYPE html>
<html lang="de">
<head>
<meta charset="utf-8">
<title>Gutschein Pflegeberatung</title>
<link rel="stylesheet" href="https://fonts.googleapis.com/css2?family=Barlow+Condensed:ital,wght@0,400;0,500;0,600;1,400&family=Work+Sans:wght@300&family=Montserrat:ital,wght@1,500;1,800&display=swap">
<style>
:root{
  --bg:#878787;
  --paper:#ffffff;
  --green:#93c01f;
  --line-green:#5aaa3c;
  --red:#c0151f;
  --ink:#2b2b2b;
  --white:#ffffff;
}
*{margin:0;padding:0;box-sizing:border-box}
html,body{width:1200px;height:1111px;overflow:hidden;background:var(--bg)}
body{position:relative;font-family:"Barlow Condensed",sans-serif;color:var(--ink)}
.card{position:absolute;left:149px;width:887px;height:443px;background:var(--paper);overflow:hidden}
.card--front{top:93px}
.card--back{top:582px}

.brand{position:absolute;display:flex;align-items:center;gap:8px;font-family:"Barlow Condensed",sans-serif;font-weight:500;color:var(--ink);letter-spacing:1px}
.brand__mark{display:block;background:var(--red)}
.brand--header{right:36px;top:44px;font-size:34px}
.brand--header .brand__mark{width:26px;height:26px}
.brand--small{font-size:20px;gap:6px}
.brand--small .brand__mark{width:15px;height:15px}

.band{position:absolute;left:0;width:100%;height:138px;background:var(--green)}
.card--front .band{top:122px}
.card--back .band{top:137px}
.photo{position:absolute;top:0;height:100%}
.photo--couple{left:0;width:263px;background:linear-gradient(100deg,#c9bfb4 0%,#e6e1da 45%,#8fa56a 80%,#dfe5d6 100%)}
.photo--autumn{left:0;width:264px;background:linear-gradient(120deg,#b5583a 0%,#6f8d3a 45%,#d1a53a 75%,#5e7a30 100%)}
.photo--carer{left:290px;width:262px;background:linear-gradient(90deg,#8a6b4a 0%,#d8b69c 40%,#e9ddd2 65%,#c4561f 100%)}

.voucher-title{position:absolute;left:284px;top:20px;font-family:"Montserrat",sans-serif;font-style:italic;font-weight:800;font-size:69px;letter-spacing:2px;color:var(--red);line-height:1}
.voucher-sub{position:absolute;left:367px;top:91px;font-family:"Montserrat",sans-serif;font-style:italic;font-weight:500;font-size:25px;letter-spacing:1.5px;color:var(--white)}

.voucher-text{position:absolute;left:285px;top:280px;width:445px;font-size:13px;line-height:16px}
.voucher-text p+p{margin-top:16px}
.voucher-valid{position:absolute;left:285px;top:408px;font-size:13px;font-style:italic}

.claim{position:absolute;left:34px;top:44px;font-family:"Work Sans",sans-serif;font-weight:300;font-size:33px;line-height:41px;color:var(--red)}
.band-text{position:absolute;left:578px;top:10px;width:272px;color:var(--white);font-size:14px;line-height:17.3px;font-weight:500}

.invite{position:absolute;left:33px;top:292px;font-family:"Montserrat",sans-serif;font-style:italic;font-weight:500;font-size:20px;color:var(--red)}
.divider{position:absolute;left:33px;top:327px;width:808px;height:1px;background:var(--line-green)}

.contact{position:absolute;top:346px;font-size:16px;line-height:20.5px}
.contact--main{left:35px}
.contact__label{display:inline-block;width:58px}
.contact strong{font-weight:600}
.branch{position:absolute;top:350px;font-size:13px;line-height:16.4px}
.branch strong{font-weight:600}
.branch--rostock{left:382px}
.branch--gnoien{left:718px}
.card--back .brand--rostock{left:260px;top:365px}
.card--back .brand--gnoien{left:599px;top:365px}
</style>
</head>
<body>

<section class="card card--front">
  <div class="brand brand--header"><span class="brand__mark"></span>PFLEGORA</div>
  <div class="band">
    <div class="photo photo--couple" role="img" aria-label="Foto: lächelndes Seniorenpaar vor hellem Fenster mit Grünpflanze"></div>
    <h1 class="voucher-title">GUTSCHEIN</h1>
    <p class="voucher-sub">zur kostenlosen Pflegeberatung</p>
  </div>
  <div class="voucher-text">
    <p>Wir unterstützen bei der Beantragung eines Pflegegrades und helfen bei abgelehnten Anträ-gen. Gerne informieren wir Sie über umfangreiche Möglichkeiten der ambulante Pflege und er-stellen einen individuellen Versorgungsplan.</p>
    <p>Darüber hinaus erhalte Sie praktische Tipps zu Alltagshilfen und konkrete Hilfestellungen rund um die Pflege, damit Sie noch so lange wie möglich zu<br>Hause bleiben können.</p>
  </div>
  <p class="voucher-valid">Gutschein gültig bis einschließlich Juli 2022</p>
</section>

<section class="card card--back">
  <h2 class="claim">Seit 10 Jahren rund um die Uhr<br>für Sie im Einsatz.</h2>
  <div class="band">
    <div class="photo photo--autumn" role="img" aria-label="Foto: Seniorenpaar im Herbstgarten mit buntem Laubstrauß"></div>
    <div class="photo photo--carer" role="img" aria-label="Foto: lachende Pflegerin umarmt eine ältere Dame"></div>
    <p class="band-text">Auf die Rückseite bitte eine kurze Info zu unserem 10 Jährigen bestehen. Lorem ipsum dolor sit amet, consectetuer adipiscing elit, sed diam nonummy nibh euismod tincidunt ut laoreet dolore magna aliquam erat volutpat. Ut wisi enim ad minim veniam, quis nostrud exerci tation ullamcorper suscipit lobortis nisl ut aliquip ex ea commodo consequat.</p>
  </div>
  <p class="invite">Wir beraten Sie gerne.</p>
  <div class="divider"></div>
  <div class="contact contact--main">
    <strong>Kontakt:</strong><br>
    <span class="contact__label">Telefon:</span> +49 (0) 39970 / 512640<br>
    <span class="contact__label">E-Mail:</span> info@pflegora.de<br>
    <strong>www.Pflegora.de</strong>
  </div>
  <div class="brand brand--small brand--rostock"><span class="brand__mark"></span>PFLEGORA</div>
  <div class="branch branch--rostock">
    <strong>Pflegora Ambulante Pflege GmbH</strong><br>
    Lindenweg 14<br>
    18055 Rostock<br>
    Tel. 0381- 40526718
  </div>
  <div class="brand brand--small brand--gnoien"><span class="brand__mark"></span>PFLEGORA</div>
  <div class="branch branch--gnoien">
    <strong>Niederlassung in Gnoien:</strong><br>
    Birkenallee 21<br>
    17179 Gnoien<br>
    Tel. 039970 512640
  </div>
</section>

</body>
</html>
```